Business Card Design and Stationary design for consulting firm

Harbourline Sourcing are looking for a new business card design and a design for their A4 letterhead / A4 invoices.

We are seeking to heavily increase our brand awareness and require a business card that's professional in appearance but also shows flare and innovation. A card design that people will remember.

About Us
Harbourline Sourcing are `The Sourcing Crew’.
Our mission is to be one of Australia’s greatest companies. Our aim is to help our customers achieve the best result from their purchasing experience.

Our Requirement:
• IMPACT! IMPACT! IMPACT!
• BUSINESS & PROFESSIONAL LOOKING

• Our business colours are orange, blue and green (See the logo attached).

We have provided an Art Design specification (attached) that needs to be followed for you to win the design. This also has the font, which is used on the logo.

We are after a two sided business card

Side One should have the:
The company Logo
The Sourcing Crew
www.harbourlinesourcing.com.au
Procure | Personnel | Probity & Privacy
Sydney | Melbourne | Adelaide | Brisbane

Side Two
Logo (optional)
Harbourline Sourcing (optional)
Employee details (details listed below)

The above format is our preferred option, but if you think you can come up with something better, feel free to put it forward.

We are leaving the design up to you, but it must incorporate the logo.

We will need a template that we can change the employee details on, as we will be adding more staff over the coming months.

The details below are for one employee per card with the same design.
------------------------

Employee Details:

Marcus Del Arroyo MBA, MMgmtStratProc
Principal Consultant
0491 372 618
Marcus@harbourlinesourcing.com.au

Brianna Tolley
Consulting Manager
0462 915 308
Brianna@harbourlinesourcing.com.au

Our website is www.harbourlinesourcing.com.au

The Letterhead / invoice needs to incorporate:
the company Logo
The Sourcing Crew
Sydney | Melbourne | Adelaide | Brisbane but otherwise the design is over to you.

This file needs to be delivered in word format as other detail will be added to the documents.

We look forward to you award winning designs. If you require any further information please feel free to contact us.

Regards
Harbourline Sourcing

Target Market(s)

Our Target market is companies with 80+ employees. The market we segment is heavily male based, between the ages of 35-55 years of age.

Industry/Entity Type

Consulting

Contact Information for Business Card

See Project Description

Font styles to use
Other font styles liked:
• See Art Specification

Requirements
Must have
• Company Colours, See Project Description
Should not have
• Be outside the Art specification guidelines

```html
<!DOCTYPE html>
<html lang="en">
<head>
<meta charset="utf-8">
<title>Harbourline Sourcing — Stationery Set</title>
<link href="https://fonts.googleapis.com/css2?family=Hind:wght@400;500;600&family=Arimo:wght@400;500&family=Kaushan+Script&display=swap" rel="stylesheet">
<style>
:root{
  --bg:#e4e4e6;
  --paper:#ffffff;
  --ink:#2f2f31;
  --ink-soft:#4a4a4c;
  --charcoal:#3a3a3c;
  --orange:#f26b25;
  --orange-light:#f7a13a;
  --grey-cell:#ececec;
  --grey-line:#d6d6d6;
  --white:#ffffff;
}
*{box-sizing:border-box;margin:0;padding:0}
html,body{width:1189px;height:1200px;overflow:hidden;background:var(--bg)}
body{font-family:"Hind",Arial,sans-serif;color:var(--ink);position:relative}
.piece{position:absolute;background:var(--paper);overflow:hidden;box-shadow:0 1px 2px rgba(0,0,0,.08)}
.abs{position:absolute}

/* brand name block */
.brand{position:absolute;display:flex;flex-direction:column;align-items:center;color:var(--charcoal);font-weight:500;text-transform:uppercase;text-align:center;line-height:1.05}
.brand-dot{border-radius:50%;background:var(--orange);margin-bottom:6px}

/* letterhead */
.letterhead{left:143px;top:127px;width:508px;height:657px}
.tagline{position:absolute;text-transform:uppercase;font-weight:500;color:var(--ink);letter-spacing:.2px}
.contact-list{position:absolute;text-align:right;color:var(--ink-soft)}
.contact-list li{list-style:none;display:flex;justify-content:flex-end;align-items:center;gap:3px}
.contact-list .ico{display:inline-block;background:var(--orange);border-radius:1px}
.recipient{left:48px;top:188px;font-family:"Arimo",Arial,sans-serif}
.recipient .name{font-size:11px;font-weight:500;text-transform:uppercase;margin-bottom:4px}
.recipient p{font-size:9px;line-height:10px}
.letter-body{left:48px;top:254px;width:414px;font-family:"Arimo",Arial,sans-serif;font-size:9.6px;line-height:14.9px;color:var(--ink)}
.letter-body p+p{margin-top:14px}
.signoff{left:48px;top:512px;font-family:"Arimo",Arial,sans-serif;font-size:9.5px}
.signature{left:46px;top:528px;font-family:"Kaushan Script",cursive;font-size:32px;color:var(--ink)}
.signer{left:48px;top:575px;font-family:"Arimo",Arial,sans-serif;font-size:10px;line-height:12px}
.signer .n{font-weight:500}
.stripe{position:absolute;left:0;width:100%;background:linear-gradient(90deg,var(--orange),var(--orange-light))}
.footer-band{position:absolute;left:0;width:100%;background:var(--charcoal);color:var(--white);display:flex;align-items:center;justify-content:center;white-space:nowrap}

/* invoice */
.invoice{left:710px;top:295px;width:342px;height:488px}
.invoice-box{left:174px;top:79px;width:147px}
.invoice-title{height:29px;background:linear-gradient(180deg,var(--orange-light),var(--orange));color:var(--white);font-weight:600;font-size:15px;display:flex;align-items:center;justify-content:center;letter-spacing:.3px}
.invoice-meta{height:26px;background:var(--grey-cell);display:grid;grid-template-columns:repeat(3,1fr);font-size:4px;color:#777;text-transform:uppercase;text-align:center;padding-top:6px}
.items{left:20px;top:171px;width:301px;border-collapse:collapse;table-layout:fixed}
.items th{height:23px;background:linear-gradient(180deg,var(--orange),var(--orange-light));color:var(--white);font-weight:400;font-size:9.5px;text-align:center}
.items th:first-child{text-align:left;padding-left:18px}
.items td{height:33px;background:var(--grey-cell);border-right:1px solid var(--grey-line);border-bottom:1px solid var(--grey-line)}
.items td:last-child{border-right:none}
.totals{left:224px;top:392px;width:97px;font-size:6px;text-transform:uppercase}
.totals .sub{height:29px;background:linear-gradient(90deg,var(--orange),var(--orange-light));color:var(--white);padding:9px 0 0 10px;line-height:9px}
.totals .grand{height:18px;background:var(--grey-cell);padding:6px 0 0 12px;color:var(--ink)}

/* business cards */
.card-front{left:143px;top:854px;width:354px;height:201px}
.card-back{left:698px;top:854px;width:353px;height:200px;background:linear-gradient(180deg,var(--orange-light),var(--orange) 95%)}
.person{position:absolute;right:16px;top:32px;text-align:right}
.person .name{font-size:15px;font-weight:500;color:var(--orange);line-height:15px}
.person .role{font-size:11px;color:var(--ink);line-height:12px}
.card-band{position:absolute;left:0;top:121px;width:100%;height:60px;background:linear-gradient(180deg,var(--orange-light),var(--orange))}
.card-contact{position:absolute;color:var(--white);font-size:10.5px;line-height:12.5px}
.card-contact li{list-style:none;display:flex;align-items:center;gap:4px}
.back-lines{position:absolute;left:0;width:100%;top:142px;text-align:center;font-size:9.5px;line-height:11px;font-weight:500;color:var(--charcoal)}
</style>
</head>
<body>

<!-- Letterhead -->
<section class="piece letterhead" aria-label="Letterhead">
  <div class="brand" style="left:40px;top:40px;width:150px;font-size:17px">
    <span class="brand-dot" style="width:26px;height:26px"></span>
    <span>Harbourline</span><span>Sourcing</span>
  </div>
  <div class="tagline" style="right:46px;top:56px;font-size:13px">The Sourcing Crew</div>
  <ul class="contact-list" style="right:46px;top:84px;font-size:8.6px;line-height:11px">
    <li>0462 915 308 <span class="ico" style="width:7px;height:7px"></span></li>
    <li>Brianna@harbourlinesourcing.com.au <span class="ico" style="width:7px;height:7px"></span></li>
    <li>www.harbourlinesourcing.com.au <span class="ico" style="width:7px;height:7px"></span></li>
  </ul>

  <div class="abs recipient">
    <div class="name">Daniel Holt</div>
    <p>Street Name,City Name.</p>
    <p>Zip Coad 0000</p>
  </div>

  <div class="abs letter-body">
    <p>Lorem Ipsum is simply dummy text of the printing and typesetting industry. Lorem Ipsum has been the industry’s standard dummy text ever since the 1500s, when an unknown printer took a galley of type and scrambled it to make a type specimen book. It has survived not only five centuries, but also the leap into electronic typesetting, remaining essentially unchanged. It was popularised in the 1960s with the release of Typerset sheets containing Lorem Ipsum passages, and more recently with desktop publishing software like Folio PageSetter including versions of Lorem Ipsum.</p>
    <p>It is a long established fact that a reader will be distracted by the readable content of a page when looking at its layout. The point of using Lorem Ipsum is that it has a more-or-less normal distribution of letters, as opposed to using ’Content here, content here’, making it look like readable English. Many desktop publishing packages and web page editors now use Lorem Ipsum as their default model text, and a search for ’lorem ipsum’ will uncover many web sites still in their infancy. Various versions have evolved over the years, sometimes by accident, sometimes on purpose (injected humour and the like).</p>
  </div>

  <div class="abs signoff">Regards,</div>
  <div class="abs signature">Jordan Vale</div>
  <div class="abs signer"><div class="n">Jordan Vale</div><div>General Maneger</div></div>

  <div class="stripe" style="top:617px;height:8px"></div>
  <div class="footer-band" style="top:625px;height:32px;font-size:12px">Procure | Personnel | Probity &amp; Privacy | Sydney | Melbourne | Adelaide | Brisbane</div>
</section>

<!-- Invoice -->
<section class="piece invoice" aria-label="Invoice">
  <div class="brand" style="left:14px;top:24px;width:120px;font-size:13px">
    <span class="brand-dot" style="width:22px;height:22px"></span>
    <span>Harbourline</span><span>Sourcing</span>
  </div>
  <div class="tagline" style="right:21px;top:25px;font-size:11px">The Sourcing Crew</div>
  <ul class="contact-list" style="right:21px;top:45px;font-size:7.6px;line-height:9px">
    <li>0462 915 308 <span class="ico" style="width:6px;height:6px"></span></li>
    <li>Brianna@harbourlinesourcing.com.au <span class="ico" style="width:6px;height:6px"></span></li>
    <li>www.harbourlinesourcing.com.au <span class="ico" style="width:6px;height:6px"></span></li>
  </ul>

  <div class="abs invoice-box">
    <div class="invoice-title">INVOICE</div>
    <div class="invoice-meta"><span>Total Due</span><span>Invoice Date :</span><span>Invoice No :</span></div>
  </div>

  <table class="abs items">
    <colgroup><col style="width:150px"><col style="width:54px"><col style="width:54px"><col style="width:43px"></colgroup>
    <thead><tr><th>Item Description</th><th>Unit Price</th><th>Quantity</th><th>Total</th></tr></thead>
    <tbody>
      <tr><td></td><td></td><td></td><td></td></tr>
      <tr><td></td><td></td><td></td><td></td></tr>
      <tr><td></td><td></td><td></td><td></td></tr>
      <tr><td></td><td></td><td></td><td></td></tr>
      <tr><td></td><td></td><td></td><td></td></tr>
      <tr><td></td><td></td><td></td><td></td></tr>
    </tbody>
  </table>

  <div class="abs totals">
    <div class="sub">Sub Text :<br>Tax Vat &nbsp;:</div>
    <div class="grand">Total &nbsp;:</div>
  </div>

  <div class="stripe" style="top:456px;height:7px"></div>
  <div class="footer-band" style="top:463px;height:25px;font-size:7.6px">Procure | Personnel | Probity &amp; Privacy | Sydney | Melbourne | Adelaide | Brisbane</div>
</section>

<!-- Business card: employee side -->
<section class="piece card-front" aria-label="Business card, employee side">
  <div class="brand" style="left:14px;top:22px;width:126px;font-size:14px">
    <span class="brand-dot" style="width:22px;height:22px"></span>
    <span>Harbourline</span><span>Sourcing</span>
  </div>
  <div class="person">
    <div class="name">Brianna Tolley</div>
    <div class="role">Consulting Manager</div>
  </div>
  <div class="tagline" style="right:16px;top:99px;font-size:11px">The Sourcing Crew</div>

  <div class="card-band"></div>
  <ul class="card-contact" style="left:18px;top:142px">
    <li>
      <svg width="9" height="10" viewBox="0 0 9 10" aria-hidden="true"><rect x="1" y="0.5" width="7" height="9" rx="1" fill="none" stroke="#fff"/><rect x="2.5" y="2" width="4" height="4" fill="#fff"/></svg>
      0462 915 308
    </li>
    <li>
      <svg width="10" height="8" viewBox="0 0 10 8" aria-hidden="true"><rect x="0.5" y="0.5" width="9" height="7" fill="#fff"/><path d="M0.5 0.5 L5 4.5 L9.5 0.5" fill="none" stroke="#f26b25"/></svg>
      Brianna@harbourlinesourcing.com.au
    </li>
  </ul>
  <div class="card-contact" style="right:16px;top:130px;text-align:right">
    14 Carrow Lane<br>Kellyville Heights<br>New South Wales 2155
  </div>
  <div class="footer-band" style="top:181px;height:20px;font-size:11px">www.harbourlinesourcing.com.au</div>
</section>

<!-- Business card: brand side -->
<section class="piece card-back" aria-label="Business card, brand side">
  <div class="brand" style="left:0;top:40px;width:100%;font-size:19px">
    <span class="brand-dot" style="width:30px;height:30px;background:var(--charcoal)"></span>
    <span>Harbourline Sourcing</span>
  </div>
  <div class="back-lines">Procure | Personnel | Probity &amp; Privacy | Sydney<br>Melbourne | Adelaide | Brisbane</div>
  <div class="footer-band" style="top:180px;height:20px;font-size:11px">www.harbourlinesourcing.com.au</div>
</section>

</body>
</html>
```